My Coffee beans packaging design

Our company named Tamsel Coffee,We are a new coffee Roasters in CHINA. We need a packaging design for our new coffee beans we roasted.We would like to see designs that use bright color. The final design should communicate the professional and modern sense.We want to catch customers eyes.We would like it is outstanding.It is a freestyle design project.We would like to see different styles.Thank you for reading our requirement.
Updates

Reason: Thank you for designing these for us,we want some more design.

Target Market(s)

All the people who love coffee

Industry/Entity Type

Coffee Shop

Font styles to use
Serif
Sans Serif
Decorative
Script

Requirements
Must have
• We do not have anything must haves.
Nice to have
• We do not have anything must haves
Should not have
• We do not have anything mustn't haves

```html
<!DOCTYPE html>
<html lang="en">
<head>
<meta charset="utf-8">
<title>Tamsel Coffee – Coffee Beans Packaging</title>
<link href="https://fonts.googleapis.com/css2?family=Oswald:wght@600;700&display=swap" rel="stylesheet">
<style>
  :root {
    --backdrop: #e9e9e9;
    --gold-deep: #c9861c;
    --gold-mid: #e8b847;
    --gold-light: #f6df9a;
    --gold-pale: #fbf1d4;
    --bean-red: #a3281c;
    --bean-red-soft: #b8452a;
    --title-orange: #e0531f;
    --title-orange-light: #f07a2a;
    --title-red: #8e1a16;
    --brand-ink: #7a2a22;
  }
  * { margin: 0; padding: 0; box-sizing: border-box; }
  html, body {
    width: 800px;
    height: 1200px;
    overflow: hidden;
    background: var(--backdrop);
  }
  .canvas {
    position: relative;
    width: 800px;
    height: 1200px;
  }
  .pack-front {
    position: absolute;
    left: 110px;
    top: 100px;
    width: 580px;
    height: 1000px;
    overflow: hidden;
    background:
      radial-gradient(circle at 50% 86%, var(--gold-pale) 0 13%, rgba(251,241,212,0) 30%),
      linear-gradient(180deg, var(--gold-deep) 0%, var(--gold-mid) 30%, var(--gold-light) 62%, var(--gold-mid) 80%, var(--gold-deep) 100%);
  }
  .bean-pattern {
    position: absolute;
    left: 24px;
    top: 24px;
    width: 532px;
    height: 366px;
    border-radius: 18px;
    background: linear-gradient(180deg, var(--bean-red) 0%, var(--bean-red-soft) 55%, rgba(184,69,42,0.35) 100%);
  }
  .product-title {
    position: absolute;
    left: 0;
    width: 100%;
    text-align: center;
    font-family: "Oswald", sans-serif;
    font-weight: 700;
    line-height: 1;
  }
  .product-title--coffee {
    top: 400px;
    font-size: 150px;
    letter-spacing: 14px;
    padding-left: 14px;
    background: linear-gradient(180deg, var(--title-orange-light), var(--title-orange));
    -webkit-background-clip: text;
    background-clip: text;
    color: transparent;
  }
  .product-title--beans {
    top: 548px;
    font-size: 134px;
    letter-spacing: 10px;
    padding-left: 10px;
    color: var(--title-red);
  }
  .brand {
    position: absolute;
    left: 0;
    top: 840px;
    width: 100%;
    display: flex;
    flex-direction: column;
    align-items: center;
    gap: 14px;
  }
  .brand__mark {
    width: 70px;
    height: 70px;
    border-radius: 50%;
    background: var(--brand-ink);
  }
  .brand__name {
    font-family: "Oswald", sans-serif;
    font-weight: 600;
    font-size: 26px;
    letter-spacing: 4px;
    text-transform: uppercase;
    color: var(--brand-ink);
  }
</style>
</head>
<body>
  <main class="canvas">
    <section class="pack-front">
      <div class="bean-pattern" role="img" aria-label="Scattered pattern of red roasted coffee beans across the top of the pack"></div>
      <h1 class="product-title product-title--coffee">COFFEE</h1>
      <h2 class="product-title product-title--beans">BEANS</h2>
      <div class="brand">
        <span class="brand__mark"></span>
        <span class="brand__name">Tamsel Coffee</span>
      </div>
    </section>
  </main>
</body>
</html>
```